Start a weight loss Clinic

build a landing page website using the content from this websites. we want to copy all the content from slimpathcoaching.net but make page look more professional. we dont have a logo yet but url is www.brightvitalitycentre.com
https://clinicwellnessalliancegroup.net/home-page
https://www.slimpathcoaching.net/

Target Market(s)

people looking to open a weightloss clinic or a franchise opportunity

Coding

Number of Pages Required

3 page

Requirements
Must have
• copy all content from other site https://www.slimpathcoaching.net/

```html
<!DOCTYPE html>
<html lang="en">
<head>
<meta charset="utf-8">
<title>SlimPath MD – Start Your Own Weight Loss Clinic</title>
<link href="https://fonts.googleapis.com/css2?family=Poppins:wght@400;500;600;700&display=swap" rel="stylesheet">
<style>
:root{
  --blue:#073a8a;
  --blue-deep:#052c6e;
  --navy:#0b2d66;
  --red:#e2161d;
  --white:#ffffff;
  --grey:#5a6478;
  --line:#dcdfe6;
}
*{box-sizing:border-box;margin:0;padding:0}
html,body{width:1200px;height:3861px;overflow:hidden;background:var(--white);font-family:"Poppins",sans-serif;color:var(--navy)}
.page{position:relative;width:1200px;height:3861px;overflow:hidden}
.abs{position:absolute}
.btn{position:absolute;display:flex;align-items:center;justify-content:center;border-radius:20px;font-size:11px;font-weight:600;color:var(--white);background:var(--red)}
.btn.light{background:var(--white);color:var(--navy)}
.eyebrow{font-size:11px;font-weight:600;letter-spacing:2px;text-transform:uppercase}

/* hero */
.hero-band{left:0;top:0;width:602px;height:575px;background:var(--blue)}
.hero-photo{left:602px;top:0;width:598px;height:575px;background:linear-gradient(135deg,#f2f2f2,#d9d5d2 55%,#b9a8a0)}
.topbar{left:168px;top:36px;width:864px;height:64px;background:var(--white);border-radius:4px;box-shadow:0 4px 14px rgba(0,0,0,.12);display:flex;align-items:center;justify-content:space-between;padding:0 28px}
.brand{display:flex;align-items:center;gap:8px;font-size:17px;font-weight:600;color:var(--navy)}
.brand i{width:18px;height:18px;border-radius:50%;background:var(--red);display:block}
.call{display:flex;align-items:center;gap:12px;font-size:14px;color:var(--navy);line-height:1.25}
.call b{font-weight:600;display:block}
.hero-copy{left:168px;top:190px;width:420px;color:var(--white)}
.hero-copy h1{font-size:45px;line-height:1.17;font-weight:600;margin:10px 0 16px}
.hero-copy p{font-size:12px;line-height:1.75}

/* welcome */
.welcome-photo{left:168px;top:653px;width:472px;height:490px;background:linear-gradient(160deg,#d8d8d8,#b0b4b8 50%,#7d8a86)}
.video-tab{left:502px;top:653px;width:140px;height:140px;background:var(--white);text-align:center;padding-top:24px;font-size:16px;line-height:1.2;color:var(--navy)}
.play{width:32px;height:32px;border-radius:50%;background:var(--red);margin:12px auto 0;display:flex;align-items:center;justify-content:center}
.inset-photo{left:274px;top:922px;width:258px;height:238px;background:linear-gradient(135deg,#eee8e6,#cdbfbd);border:4px solid var(--white)}
.welcome-copy{left:682px;top:692px;width:365px}
.welcome-copy h2{font-size:31px;font-weight:600;margin:6px 0 2px}
.welcome-copy h3{font-size:18px;font-weight:400;color:var(--red);margin-bottom:18px}
.welcome-copy p{font-size:12px;line-height:1.72;color:var(--grey);margin-bottom:20px}
.welcome-copy p b{color:var(--navy);font-weight:600}
.welcome-copy .happy{font-size:15px;color:var(--red);margin-bottom:26px}
.ask{font-size:11px;font-weight:600;color:var(--red);text-decoration:underline}

/* offer */
.offer-band{left:0;top:1243px;width:1200px;height:535px;background:var(--blue)}
.offer-title{left:0;top:1312px;width:1200px;text-align:center;font-size:38px;font-weight:600;color:var(--white)}
.card{position:absolute;top:1397px;width:226px;height:266px;background:var(--white);border-radius:3px;text-align:center;padding-top:30px}
.card.active{background:var(--red);color:var(--white)}
.card .ic{width:100px;height:100px;border-radius:50%;margin:0 auto;background:var(--blue);border:3px solid var(--red);display:flex;align-items:center;justify-content:center}
.card.active .ic{background:var(--red);border-color:var(--white)}
.card h4{font-size:16px;font-weight:400;line-height:1.25;margin-top:22px;height:48px}
.card .btn{position:static;margin:14px auto 0;width:116px;height:32px}

/* steps */
.steps-head{left:0;top:1853px;width:1200px;text-align:center}
.steps-head h2{font-size:36px;font-weight:600;letter-spacing:1px;margin-top:4px}
.step-photo{top:1950px;width:275px;height:275px;border-radius:50%}
.step-btn{position:absolute;top:2148px;width:278px;height:52px;background:var(--red);color:var(--white);font-size:19px;font-weight:600;display:flex;align-items:center;justify-content:center;border-radius:3px}

/* compare */
.compare-band{left:0;top:2305px;width:602px;height:575px;background:var(--blue)}
.compare-photo{left:602px;top:2305px;width:598px;height:575px;background:linear-gradient(140deg,#8a6a4a,#b38a60 45%,#d8c6a8 80%,#ede5d6)}
.compare-copy{left:168px;top:2398px;color:var(--white)}
.compare-copy h2{font-size:37px;font-weight:600;margin-bottom:6px}
.compare-copy li{list-style:none;font-size:19px;line-height:34.5px;display:flex;align-items:center;gap:7px}

/* contact */
.contact-head{left:0;top:2958px;width:1200px;text-align:center}
.contact-head h2{font-size:40px;font-weight:500;margin-top:4px}
.field{position:absolute;border:1px solid var(--line);font-size:10px;color:var(--grey);padding:14px 14px;background:var(--white)}
.field.focus{border-color:var(--red)}

/* footer */
.footer-band{left:0;top:3400px;width:1200px;height:461px;background:var(--blue-deep)}
.foot-col{color:var(--white)}
.foot-col h5{font-size:14px;font-weight:600;margin-bottom:10px}
.foot-rule{width:40px;height:1px;background:rgba(255,255,255,.6);margin-bottom:26px}
.info-row{display:flex;align-items:center;gap:14px;font-size:11px;line-height:1.3;margin-bottom:26px}
.info-row span.dot{width:38px;height:38px;border-radius:50%;background:var(--red);display:flex;align-items:center;justify-content:center;flex:none}
.links li{list-style:none;font-size:11px;line-height:34.5px}
.divider{top:3520px;width:1px;height:300px;background:rgba(255,255,255,.25)}
.foot-brand{left:430px;top:3560px;width:340px;text-align:center;color:var(--white);font-size:30px;font-weight:500;display:flex;align-items:center;justify-content:center;gap:12px}
.foot-brand i{width:34px;height:34px;border-radius:50%;background:var(--white);display:block}
.socials{left:506px;top:3668px;display:flex;gap:14px}
.socials span{width:36px;height:36px;border-radius:50%;background:var(--red);display:block}
.copyright{left:0;top:3830px;width:1200px;text-align:center;font-size:11px;color:var(--white)}
</style>
</head>
<body>
<div class="page">

  <!-- Hero -->
  <section>
    <div class="abs hero-band"></div>
    <div class="abs hero-photo" role="img" aria-label="Doctor measuring a patient's waist with a tape measure in a bright clinic"></div>
    <svg class="abs" style="left:0;top:500px" width="1200" height="80" viewBox="0 0 1200 80" preserveAspectRatio="none">
      <path d="M0 28 Q300 90 602 60 L602 80 L0 80 Z" fill="#fff"/>
      <path d="M602 70 Q900 60 1200 28 L1200 80 L602 80 Z" fill="#fff"/>
    </svg>
    <header class="abs topbar">
      <div class="brand"><i></i>SlimPath MD</div>
      <div class="call">
        <svg width="30" height="30" viewBox="0 0 24 24" fill="none" stroke="#e2161d" stroke-width="1.6"><path d="M5 3h4l2 5-2.5 1.5a11 11 0 0 0 6 6L16 13l5 2v4a2 2 0 0 1-2 2A16 16 0 0 1 3 5a2 2 0 0 1 2-2z"/></svg>
        <div><b>Call Us:</b>(555) 014-2386</div>
      </div>
    </header>
    <div class="abs hero-copy">
      <div class="eyebrow">Start your own</div>
      <h1>Profitable Weight Loss Clinic!</h1>
      <p>We are not a weight loss franchise – you are simply buying our business model, training and support for one low fee. Please read about us, look at what we offer.</p>
    </div>
    <div class="btn light" style="left:168px;top:415px;width:110px;height:32px">Learn More</div>
  </section>

  <!-- Welcome -->
  <section>
    <div class="abs welcome-photo" role="img" aria-label="Laptop with a diet plan spreadsheet, clipboard and potted plant on a desk"></div>
    <div class="abs video-tab">Watch<br>Video
      <div class="play"><svg width="12" height="12" viewBox="0 0 12 12"><path d="M3 1l8 5-8 5z" fill="#fff"/></svg></div>
    </div>
    <div class="abs inset-photo" role="img" aria-label="Waist being measured with a yellow tape measure"></div>
    <div class="abs welcome-copy">
      <div class="eyebrow" style="font-size:10px">Welcome there!</div>
      <h2>Start Your Own</h2>
      <h3>Weight Loss &amp; Wellness Center</h3>
      <p>SlimPath MD now offers our model to you so you can add <b>weight loss and wellness programs</b> to your existing medical practice or open a stand alone weight loss and wellness center.</p>
      <p>We are not a <b>weight loss franchise – you are simply buying our business model</b>, training and support for one low fee. Please read about us, look at what we offer and compare us to <b>weight loss franchises</b> in the marketplace.</p>
      <p>We now offer you a free market analysis and sample break even analysis for your area. <b>Please see our contact page.</b></p>
      <p class="happy">We think you will be happy you found us!</p>
      <span class="ask">Ask An Expert</span>
    </div>
    <div class="btn" style="left:779px;top:1096px;width:110px;height:34px">More Info</div>
  </section>

  <!-- What We Offer -->
  <section>
    <div class="abs offer-band"></div>
    <svg class="abs" style="left:0;top:1720px" width="1200" height="60" viewBox="0 0 1200 60" preserveAspectRatio="none"><path d="M0 8 Q600 -30 1200 8 L1200 60 L0 60 Z" fill="#fff"/></svg>
    <h2 class="abs offer-title">What We Offer</h2>
    <div class="card active" style="left:133px">
      <div class="ic"><svg width="48" height="48" viewBox="0 0 48 48" fill="none" stroke="#fff" stroke-width="2"><rect x="14" y="6" width="20" height="14"/><circle cx="12" cy="28" r="4"/><circle cx="36" cy="28" r="4"/><path d="M4 42v-4a8 8 0 0 1 16 0v4M28 42v-4a8 8 0 0 1 16 0v4M20 40h8"/></svg></div>
      <h4>One-on-one business<br>&amp; medical training</h4>
      <div class="btn light">Read More</div>
    </div>
    <div class="card" style="left:369px">
      <div class="ic"><svg width="48" height="48" viewBox="0 0 48 48" fill="none" stroke="#fff" stroke-width="2"><rect x="8" y="8" width="12" height="12"/><rect x="28" y="8" width="12" height="12"/><rect x="28" y="28" width="12" height="12"/><circle cx="14" cy="34" r="6"/></svg></div>
      <h4>Marketing &amp; Advertising<br>Training</h4>
      <div class="btn">Read More</div>
    </div>
    <div class="card" style="left:606px">
      <div class="ic"><svg width="48" height="48" viewBox="0 0 48 48" fill="none" stroke="#fff" stroke-width="2"><rect x="12" y="6" width="24" height="32"/><path d="M18 14h12M18 20h12M24 26v14M17 33h14"/></svg></div>
      <h4>Diets, Patient Protocols<br>&amp; Programs</h4>
      <div class="btn">Read More</div>
    </div>
    <div class="card" style="left:843px">
      <div class="ic"><svg width="48" height="48" viewBox="0 0 48 48" fill="none" stroke="#fff" stroke-width="2"><rect x="10" y="6" width="24" height="34"/><path d="M16 14h12M16 20h12M16 26h8M30 30l8 8"/></svg></div>
      <h4>Office &amp; Operations<br>Manuals</h4>
      <div class="btn">Read More</div>
    </div>
  </section>

  <!-- Get Started -->
  <section>
    <div class="abs steps-head">
      <div class="eyebrow" style="color:var(--red);font-size:10px">It's easy</div>
      <h2>GET STARTED TODAY</h2>
    </div>
    <div class="abs step-photo" style="left:145px;background:linear-gradient(135deg,#8fb07a,#4d6b3f 60%,#2c2c2c)" role="img" aria-label="Hands holding a smartphone"></div>
    <div class="abs step-photo" style="left:463px;background:linear-gradient(135deg,#c7704d,#a85a3f 50%,#e3b54a)" role="img" aria-label="Visitor with a yellow coat walking toward a brick building"></div>
    <div class="abs step-photo" style="left:781px;background:linear-gradient(135deg,#3a3a3a,#d9dde2 50%,#f2f2f2)" role="img" aria-label="Person joining a video webinar on a monitor"></div>
    <div class="step-btn" style="left:143px">Contact Us</div>
    <div class="step-btn" style="left:461px">Visit Us</div>
    <div class="step-btn" style="left:779px">Schedule A Webinar</div>
  </section>

  <!-- Compare -->
  <section>
    <div class="abs compare-band"></div>
    <div class="abs compare-photo" role="img" aria-label="Clinic reception desk with a wood-panelled wall and flowers"></div>
    <svg class="abs" style="left:0;top:2810px" width="1200" height="75" viewBox="0 0 1200 75" preserveAspectRatio="none"><path d="M0 22 Q300 60 602 66 L602 75 L0 75 Z" fill="#fff"/></svg>
    <div class="abs compare-copy">
      <h2>Our COMPARE</h2>
      <ul>
        <li><svg width="14" height="14" viewBox="0 0 14 14" fill="none" stroke="#fff" stroke-width="1.3"><circle cx="7" cy="7" r="6"/><path d="M4 7l2 2 4-4"/></svg>No franchise fees</li>
        <li><svg width="14" height="14" viewBox="0 0 14 14" fill="none" stroke="#fff" stroke-width="1.3"><circle cx="7" cy="7" r="6"/><path d="M4 7l2 2 4-4"/></svg>No Territory fees</li>
        <li><svg width="14" height="14" viewBox="0 0 14 14" fill="none" stroke="#fff" stroke-width="1.3"><circle cx="7" cy="7" r="6"/><path d="M4 7l2 2 4-4"/></svg>No monthly licensing fees</li>
        <li><svg width="14" height="14" viewBox="0 0 14 14" fill="none" stroke="#fff" stroke-width="1.3"><circle cx="7" cy="7" r="6"/><path d="M4 7l2 2 4-4"/></svg>No % advertising fees</li>
        <li><svg width="14" height="14" viewBox="0 0 14 14" fill="none" stroke="#fff" stroke-width="1.3"><circle cx="7" cy="7" r="6"/><path d="M4 7l2 2 4-4"/></svg>No scope of practice limits</li>
        <li><svg width="14" height="14" viewBox="0 0 14 14" fill="none" stroke="#fff" stroke-width="1.3"><circle cx="7" cy="7" r="6"/><path d="M4 7l2 2 4-4"/></svg>No convention fees</li>
        <li><svg width="14" height="14" viewBox="0 0 14 14" fill="none" stroke="#fff" stroke-width="1.3"><circle cx="7" cy="7" r="6"/><path d="M4 7l2 2 4-4"/></svg>No % royalties</li>
        <li><svg width="14" height="14" viewBox="0 0 14 14" fill="none" stroke="#fff" stroke-width="1.3"><circle cx="7" cy="7" r="6"/><path d="M4 7l2 2 4-4"/></svg>No mandatory vendors</li>
      </ul>
    </div>
    <div class="btn" style="left:168px;top:2738px;width:116px;height:32px">Compare Now!</div>
  </section>

  <!-- Contact -->
  <section>
    <div class="abs contact-head">
      <div class="eyebrow" style="color:var(--red);font-size:10px">Contact us</div>
      <h2>Today To Learn More</h2>
    </div>
    <div class="field focus" style="left:168px;top:3052px;width:421px;height:48px">First Name*</div>
    <div class="field" style="left:611px;top:3052px;width:421px;height:48px">Last Name*</div>
    <div class="field" style="left:168px;top:3109px;width:421px;height:48px">Services*</div>
    <div class="field" style="left:611px;top:3109px;width:421px;height:48px">Phone Number*</div>
    <div class="field" style="left:168px;top:3167px;width:864px;height:95px">Enquiry*</div>
    <div class="btn" style="left:541px;top:3302px;width:117px;height:34px">Submit !</div>
  </section>

  <!-- Footer -->
  <footer>
    <div class="abs footer-band"></div>
    <svg class="abs" style="left:0;top:3395px" width="1200" height="70" viewBox="0 0 1200 70" preserveAspectRatio="none"><path d="M0 0 L1200 0 L1200 20 Q600 -20 0 68 Z" fill="#fff"/></svg>
    <div class="abs foot-col" style="left:156px;top:3535px">
      <h5>CONTACT INFO</h5>
      <div class="foot-rule"></div>
      <div class="info-row"><span class="dot"><svg width="14" height="16" viewBox="0 0 14 16"><path d="M7 0a6 6 0 0 1 6 6c0 4-6 10-6 10S1 10 1 6a6 6 0 0 1 6-6z" fill="#fff"/><circle cx="7" cy="6" r="2" fill="#e2161d"/></svg></span>4180 Meadowlark Drive<br>Suite 210, Fairview, GA 30099</div>
      <div class="info-row"><span class="dot"><svg width="16" height="16" viewBox="0 0 24 24" fill="none" stroke="#fff" stroke-width="2"><path d="M5 3h4l2 5-2.5 1.5a11 11 0 0 0 6 6L16 13l5 2v4a2 2 0 0 1-2 2A16 16 0 0 1 3 5a2 2 0 0 1 2-2z"/></svg></span>Phone: (555) 014-2386</div>
      <div class="info-row"><span class="dot"><svg width="16" height="12" viewBox="0 0 16 12" fill="none" stroke="#fff" stroke-width="1.5"><rect x="1" y="1" width="14" height="10"/><path d="M1 1l7 6 7-6"/></svg></span>info@slimpathcoaching.net</div>
    </div>
    <div class="abs divider" style="left:424px"></div>
    <div class="abs divider" style="left:778px"></div>
    <div class="abs foot-brand"><i></i>SlimPath MD</div>
    <div class="abs socials"><span></span><span></span><span></span><span></span></div>
    <div class="abs foot-col" style="left:847px;top:3535px">
      <h5>QUICK LINKS</h5>
      <div class="foot-rule" style="margin-bottom:8px"></div>
      <ul class="links">
        <li>HOME</li><li>ABOUT US</li><li>WHAT WE OFFER</li><li>COMPARE</li><li>FAQ</li><li>CONTACT</li>
      </ul>
    </div>
    <div class="abs copyright">© 2023 SlimPath MD, Inc. All rights reserved</div>
  </footer>

</div>
</body>
</html>
```